Business Card Design for new logo

Business card Design for new logo. Follow colors from logo.
The company has offices in multiple comtries
Want to have some bulltes on the countries and also on the main services

Something like
USA*Dominican Republic*LATAM

Consulting*Healthcare IT*Tranformation

Industry/Entity Type

Information Technology

Contact Information for Business Card

Address, Phones, countries, name and position

Lucan morrel

Founder and CEO

947 Tarrow Ln
Brisk hollow, PA 17990

Lmorrel@quendoxcare.com

www.quendoxcare.com

555-304-6182

555-222-2222

```html
<!DOCTYPE html>
<html lang="en">
<head>
<meta charset="utf-8">
<title>Quendox Care – Business Card</title>
<link rel="stylesheet" href="https://fonts.googleapis.com/css2?family=Merriweather:wght@700&family=Lato:wght@400&display=swap">
<style>
  :root {
    --backdrop: #4a4a4c;
    --card-dark: #1b1b1c;
    --card-light: #ffffff;
    --brand-blue: #2372b8;
    --brand-orange: #f28b4c;
    --text-dark: #2a2a2a;
    --text-light: #f4f4f4;
    --divider: #7a7a7a;
    --flag-red: #c8283b;
    --flag-navy: #24336e;
    --flag-gold: #e4b52a;
  }
  * { box-sizing: border-box; margin: 0; padding: 0; }
  html, body { width: 1200px; height: 895px; overflow: hidden; }
  body {
    background: var(--backdrop);
    font-family: "Lato", sans-serif;
    display: flex;
    align-items: center;
    justify-content: center;
    gap: 30px;
  }
  .card {
    width: 560px;
    height: 320px;
    position: relative;
    box-shadow: 0 6px 18px rgba(0,0,0,.35);
  }

  /* Front */
  .card--front {
    background: var(--card-dark);
    display: flex;
    flex-direction: column;
    align-items: center;
    justify-content: center;
  }
  .brand {
    display: flex;
    align-items: center;
    gap: 12px;
  }
  .brand__dot {
    width: 22px; height: 22px; border-radius: 50%;
    background: var(--brand-orange);
  }
  .brand__name {
    font-family: "Merriweather", serif;
    font-weight: 700;
    color: var(--brand-blue);
    font-size: 46px;
    letter-spacing: .5px;
  }
  .countries {
    display: flex;
    gap: 12px;
    margin-top: 26px;
  }
  .flag { width: 46px; height: 28px; display: block; }
  .flag--usa { background: linear-gradient(180deg, var(--flag-red), #f3f3f3 55%, var(--flag-navy)); }
  .flag--dr { background: linear-gradient(90deg, var(--flag-navy) 50%, var(--flag-red) 50%); }
  .flag--latam { background: linear-gradient(135deg, var(--flag-gold), var(--flag-red) 50%, var(--flag-navy)); }
  .services {
    margin-top: 22px;
    color: var(--text-light);
    font-size: 15px;
    letter-spacing: 2.5px;
  }

  /* Back */
  .card--back {
    background: var(--card-light);
    display: flex;
    align-items: center;
  }
  .card--back .brand { width: 290px; justify-content: center; }
  .card--back .brand__name { font-size: 34px; }
  .card--back .brand__dot { width: 16px; height: 16px; }
  .divider {
    width: 1px; height: 200px;
    background: var(--divider);
  }
  .contact { padding-left: 24px; color: var(--text-dark); }
  .contact__name {
    font-family: "Merriweather", serif;
    font-weight: 700;
    color: var(--brand-blue);
    font-size: 27px;
    line-height: 1.1;
  }
  .contact__role { font-size: 14px; margin-bottom: 14px; }
  .contact__address { font-size: 14px; line-height: 1.25; margin-bottom: 12px; }
  .contact__list { list-style: none; font-size: 14px; line-height: 1.45; }
  .contact__list li { display: flex; align-items: center; gap: 8px; }
  .icon { width: 14px; height: 14px; flex: none; }
</style>
</head>
<body>

  <section class="card card--front">
    <div class="brand">
      <span class="brand__dot"></span>
      <span class="brand__name">Quendox Care</span>
    </div>
    <div class="countries">
      <span class="flag flag--usa" role="img" aria-label="Flag of the United States"></span>
      <span class="flag flag--dr" role="img" aria-label="Flag of the Dominican Republic"></span>
      <span class="flag flag--latam" role="img" aria-label="Latin America flag"></span>
    </div>
    <p class="services">Consulting * Healthcare IT * Tranformation</p>
  </section>

  <section class="card card--back">
    <div class="brand">
      <span class="brand__dot"></span>
      <span class="brand__name">Quendox Care</span>
    </div>
    <div class="divider"></div>
    <div class="contact">
      <h1 class="contact__name">Lucan morrel</h1>
      <p class="contact__role">Founder and CEO</p>
      <p class="contact__address">947 Tarrow Ln, Brisk hollow<br>PA 17990</p>
      <ul class="contact__list">
        <li>
          <svg class="icon" viewBox="0 0 14 14" aria-hidden="true"><rect x="3" y="1" width="8" height="12" rx="1.5" fill="none" stroke="var(--brand-orange)" stroke-width="1.6"/><circle cx="7" cy="10.8" r=".9" fill="var(--brand-orange)"/></svg>
          555-304-6182
        </li>
        <li>
          <svg class="icon" viewBox="0 0 14 14" aria-hidden="true"><path d="M3 1.5l2.5 2.8-1.3 1.6c.9 1.8 2.2 3.1 4 4l1.6-1.3 2.7 2.5-1.6 1.6C6.6 12.3 1.7 7.4 1.4 3.1z" fill="var(--brand-orange)"/></svg>
          555-222-2222
        </li>
        <li>
          <svg class="icon" viewBox="0 0 14 14" aria-hidden="true"><rect x="1" y="3" width="12" height="8.5" fill="var(--brand-orange)"/><path d="M1 3l6 4.8L13 3" fill="none" stroke="#fff" stroke-width="1.2"/></svg>
          Lmorrel@quendoxcare.com
        </li>
        <li>
          <svg class="icon" viewBox="0 0 14 14" aria-hidden="true"><g fill="none" stroke="var(--brand-orange)" stroke-width="1.2"><circle cx="7" cy="7" r="5.8"/><ellipse cx="7" cy="7" rx="2.6" ry="5.8"/><path d="M1.2 7h11.6M2.2 4h9.6M2.2 10h9.6"/></g></svg>
          www.quendoxcare.com
        </li>
      </ul>
    </div>
  </section>

</body>
</html>
```